Eye-Catching, Direct Marketing Residential Painting Flyer!

I am run a residential painting business and am looking for a flyer to be designed to mailout to potential customers.
I want the copy/wording to be designed similar to this flyer.

It's important that the person reading the flyer gets the benefits we're promoting which is why I want the wording/copy to be almost identical to the flyer attached.

However, the structure will be different. The flyer will be a postcard thick, 5 x11.5.
Double sided.

The name of the company is Brightwall Coaters.

I would also like the prominent colour to either be light green or orange.

Target Market(s)

Home Owners between the age of 45-80.

Industry/Entity Type

Painting And Decorating

Font styles to use
Serif

Colors
f68d4d
faa54b
f78f20
f37122
9bcb3c
abd037
cadf82

Requirements
Must have
• Excellent Eye-Catching Design
• Benefits Visibly Promoted
• Action Taking Incentive- Call Now for FREE Window Cleaning and FREE Painting Estimate
Should not have
• Crowded wording

```html
<!DOCTYPE html>
<html lang="en">
<head>
<meta charset="utf-8">
<title>Brightwall Coaters – Brochure</title>
<link href="https://fonts.googleapis.com/css2?family=Montserrat:ital,wght@0,400;0,600;0,700;0,800;1,400;1,700&display=swap" rel="stylesheet">
<style>
  :root{
    --orange:#f37122;
    --orange-soft:#f78f20;
    --green:#9bcb3c;
    --green-light:#abd037;
    --grey-panel:#ececec;
    --grey-text:#3a3a3a;
    --grey-pill:#6f6f6f;
    --red:#d9262b;
    --stage:#d7d7d7;
  }
  *{box-sizing:border-box;margin:0;padding:0}
  html,body{width:1200px;height:1200px;overflow:hidden}
  body{
    background:var(--stage);
    font-family:"Montserrat",Arial,sans-serif;
    color:var(--grey-text);
    position:relative;
  }
  .brochure{
    position:absolute;left:30px;top:390px;
    width:1140px;height:420px;
    display:flex;
    box-shadow:0 18px 40px rgba(0,0,0,.25);
  }
  .panel{position:relative;width:380px;height:420px;background:#fff;overflow:hidden}
  .panel + .panel{border-left:1px solid #ddd}
  .panel svg.bands{position:absolute;inset:0}

  /* Panel 1 */
  .problem{position:absolute;left:28px;top:70px;width:130px}
  .heading{color:var(--orange);font-weight:700;font-size:15px;margin-bottom:8px}
  .body-copy{font-size:10.5px;line-height:1.35}
  .problem-photo{position:absolute;left:168px;top:30px;width:188px;height:128px;background:linear-gradient(135deg,#a0623a,#6e3b1f 60%,#3b2a22);border:5px solid #fff;box-shadow:0 1px 3px rgba(0,0,0,.2)}
  .solution{position:absolute;left:32px;top:220px;width:200px}
  .painter-art{position:absolute;left:248px;top:190px;width:110px;height:110px;border-radius:50%;background:radial-gradient(circle,#6aa9d8,#2f6fb0 70%)}
  .quote{position:absolute;left:32px;top:312px;width:320px;font-size:10px;font-style:italic;line-height:1.45}
  .quote b{font-size:16px;font-style:normal;line-height:0;vertical-align:-3px}
  .attribution{position:absolute;left:32px;top:352px;color:var(--orange);font-size:11px;font-weight:600;line-height:1.2}

  /* Panel 2 */
  .offer-pill{position:absolute;left:50%;top:14px;transform:translateX(-50%);background:var(--orange);color:#fff;font-weight:800;font-size:15px;padding:5px 20px;border-radius:16px;white-space:nowrap}
  .offer-cols{position:absolute;left:18px;top:50px;right:18px;display:flex;gap:14px}
  .offer-cols p{flex:1;font-size:9px;line-height:1.3}
  .offer-cols p + p{border-left:1.5px solid var(--orange);padding-left:12px}
  .offer-cols em{color:var(--orange);font-weight:700}
  .offer-cols strong{color:var(--orange);font-weight:600}
  .team-photo{position:absolute;left:0;top:138px;width:380px;height:172px;background:linear-gradient(180deg,#8f9aa0,#c9cccf 60%,#b3b7ba)}
  .estimate{position:absolute;left:262px;top:262px;width:112px;height:100px}
  .estimate-text{position:absolute;left:262px;top:282px;width:112px;text-align:center}
  .estimate-text .free{color:var(--orange);font-weight:800;font-size:22px;line-height:1}
  .estimate-text .lbl{font-size:12px}
  .estimate-text .tel{color:var(--orange);font-weight:700;font-size:11.5px}
  .contacts{position:absolute;left:34px;top:352px;font-size:11.5px;line-height:1.5}
  .contacts span{display:inline-block;width:8px;height:8px;border-radius:50%;background:var(--orange);margin-right:10px}

  /* Panel 3 */
  .brand{position:absolute;left:100px;top:22px;display:flex;align-items:center;gap:6px;color:var(--grey-text);font-weight:700;font-size:13px;letter-spacing:.5px}
  .brand i{width:9px;height:9px;border-radius:50%;background:var(--red);display:block}
  .brand-rule{position:absolute;left:100px;top:44px;width:150px;height:2px;background:var(--red)}
  .tagline{position:absolute;left:22px;top:64px;font-size:12px;font-weight:800;color:var(--orange)}
  .tagline span{color:var(--grey-text);font-weight:400}
  .house-photo{position:absolute;left:0;top:90px;width:380px;height:180px;background:linear-gradient(180deg,#5e8fc9 0%,#9fc0de 35%,#3f6a32 55%,#6b8a3a 100%)}
  .rot-pill{position:absolute;left:80px;top:296px;background:var(--grey-pill);color:#fff;font-size:11px;font-weight:600;padding:3px 14px;border-radius:12px}
  .look{position:absolute;left:70px;top:322px;color:var(--orange);font-size:17px;font-weight:600}
  .promise{position:absolute;left:22px;top:350px;font-size:18px;font-weight:800;color:var(--grey-text)}
  .promise .g{color:var(--green)}
</style>
</head>
<body>
<main class="brochure">

  <section class="panel panel-problem">
    <svg class="bands" viewBox="0 0 380 420" aria-hidden="true">
      <polygon points="0,180 380,160 380,420 0,420" fill="var(--grey-panel)"/>
      <line x1="0" y1="180" x2="380" y2="160" stroke="var(--orange)" stroke-width="3"/>
      <line x1="0" y1="186" x2="380" y2="166" stroke="var(--green)" stroke-width="3"/>
      <rect x="0" y="190" width="14" height="210" fill="var(--green)"/>
      <line x1="0" y1="400" x2="380" y2="385" stroke="var(--green)" stroke-width="4"/>
      <line x1="0" y1="406" x2="380" y2="391" stroke="var(--orange)" stroke-width="2"/>
    </svg>
    <div class="problem">
      <h2 class="heading">Problem</h2>
      <p class="body-copy">Your exterior semi-transparent deck, fence or siding is peeling, chipping or faded.</p>
    </div>
    <div class="problem-photo" role="img" aria-label="Photo of a weathered wooden deck with a can of stain"></div>
    <div class="solution">
      <h2 class="heading">Solution</h2>
      <p class="body-copy">A fresh coat of stain to protect the wood and make it look clean, fresh and beautiful!</p>
    </div>
    <div class="painter-art" role="img" aria-label="Illustration of a painter holding a paint brush"></div>
    <p class="quote"><b>“</b> They provided us with the satisfaction that we chose wisely when we decided to grant the project to this company <b>”</b></p>
    <p class="attribution">Marian &amp; Victor - Elm Ridge</p>
  </section>

  <section class="panel panel-offer">
    <svg class="bands" viewBox="0 0 380 420" aria-hidden="true">
      <line x1="0" y1="30" x2="380" y2="30" stroke="var(--orange)" stroke-width="1.5"/>
      <line x1="0" y1="134" x2="380" y2="134" stroke="var(--orange)" stroke-width="2"/>
      <line x1="0" y1="312" x2="380" y2="312" stroke="var(--green)" stroke-width="4"/>
    </svg>
    <div class="offer-pill">Special Offer!</div>
    <div class="offer-cols">
      <p>If you are one of the <em>first 13 exterior projects</em> that book with us, you will receive a complimentary <strong>interior design consultation</strong> by a <strong>professional interior designer!</strong></p>
      <p>If you are one of the <em>first 17 exterior projects</em> that book with us, you will receive a complimentary <strong>window cleaning!</strong></p>
    </div>
    <div class="team-photo" role="img" aria-label="Photo of the painting crew in paint-spattered shirts"></div>
    <svg class="estimate" viewBox="0 0 112 100" aria-hidden="true">
      <polygon points="28,3 84,3 109,50 84,97 28,97 3,50" fill="#fff" stroke="var(--orange)" stroke-width="4"/>
    </svg>
    <div class="estimate-text">
      <div class="free">FREE</div>
      <div class="lbl">Estimates:</div>
      <div class="tel">555-014-2290</div>
    </div>
    <div class="contacts">
      <p><span></span>www.brightwallcoaters.example</p>
      <p><span></span>social.example/brightwallcoaters</p>
    </div>
  </section>

  <section class="panel panel-cover">
    <svg class="bands" viewBox="0 0 380 420" aria-hidden="true">
      <line x1="0" y1="88" x2="380" y2="88" stroke="var(--orange)" stroke-width="3"/>
      <line x1="0" y1="272" x2="380" y2="272" stroke="var(--green)" stroke-width="4"/>
      <line x1="0" y1="278" x2="380" y2="278" stroke="var(--orange)" stroke-width="2"/>
    </svg>
    <div class="brand"><i></i>BRIGHTWALL COATERS</div>
    <div class="brand-rule"></div>
    <p class="tagline">TAKE CONTROL OF HOW <span>YOUR HOME LOOKS!</span></p>
    <div class="house-photo" role="img" aria-label="Photo of a large freshly painted country house with lawn and trees"></div>
    <p class="rot-pill">Has the wood started to rot yet?</p>
    <p class="look">We make your home look</p>
    <p class="promise"><span class="g">CLEAN,</span> FRESH &amp; BEAUTIFUL <span class="g">AGAIN!</span></p>
  </section>

</main>
</body>
</html>
```